Sherwood Ads

Would like to have new web ads announcing opening of a new pediatric office (Larkmont Pediatrics - Sherwood). First and only dedicated pediatric clinic in Sherwood. Ads need to be following sizes: 160x160, 180x180, 300x250, 336x280, 728x90, 920x250, 1080x1080, 1200x627. Sample of previous ad attached.

```html
<!DOCTYPE html>
<html lang="en">
<head>
<meta charset="utf-8">
<title>Larkmont Pediatrics – Sherwood Web Ads</title>
<link href="https://fonts.googleapis.com/css2?family=Outfit:wght@400;500;600;700;800&family=Nunito:wght@600;700;800&family=Kaushan+Script&family=Montserrat:wght@600;700&display=swap" rel="stylesheet">
<style>
  :root{
    --board:#ece6fb;
    --violet:#5a4bb0;
    --violet-soft:#8a7ed6;
    --navy:#3a36a4;
    --blue:#3d50c8;
    --red:#ef3a2d;
    --yellow:#f6c21a;
    --ink:#3b3545;
    --white:#ffffff;
    --label:#1f1c2c;
  }
  *{box-sizing:border-box;margin:0;padding:0}
  html,body{width:1200px;height:575px;overflow:hidden;background:var(--board)}
  .board{position:relative;width:1200px;height:575px;overflow:hidden;background:var(--board);font-family:"Outfit",sans-serif}
  .sprite{position:absolute;width:0;height:0;overflow:hidden}

  .size-label{position:absolute;width:120px;text-align:center;font-family:"Montserrat",sans-serif;font-weight:600;font-size:8.5px;color:var(--label);letter-spacing:.02em}
  .size-label.big{width:240px;font-size:24px;font-weight:700;letter-spacing:0}

  .ad{position:absolute;background:var(--white);overflow:hidden;transform-origin:0 0;transform:scale(.3888)}
  .abs{position:absolute}
  .layer{position:absolute;left:0;top:0}

  .brand-mark{position:absolute;border-radius:50%;background:var(--violet)}
  .brand-name{position:absolute;font-weight:700;color:var(--violet);line-height:.98}

  .h-sher{position:absolute;font-weight:600;color:var(--violet);letter-spacing:.02em;line-height:1;white-space:nowrap}
  .h-first{position:absolute;font-weight:800;color:var(--navy);line-height:1;letter-spacing:-.01em;white-space:nowrap}
  .h-first .red{color:var(--red)}
  .h-ded{position:absolute;font-weight:500;color:var(--ink);letter-spacing:.04em;line-height:1.1;white-space:nowrap}
  .center{text-align:center}

  .pin-ring{position:absolute;border-radius:50%;background:var(--white);border:2px solid var(--violet);display:flex;align-items:center;justify-content:center;color:var(--violet)}
  .pin-ring svg{width:58%;height:58%}
  .open-band{position:absolute;background:var(--violet);color:var(--white);font-weight:600;display:flex;align-items:center;justify-content:center;white-space:nowrap;clip-path:polygon(0 0,100% 0,calc(100% - .7em) 100%,0 100%)}
  .open-band b{color:var(--yellow);font-weight:600;margin-right:.25em}
  .open-box{position:absolute;background:var(--violet);border-radius:14px;color:var(--white);font-weight:600;text-align:center;line-height:1.22;display:flex;flex-direction:column;justify-content:center}
  .open-box b{color:var(--yellow);font-weight:600}

  .care{position:absolute;font-family:"Nunito",sans-serif;font-weight:700;color:var(--ink);line-height:1.05}
  .care em{font-style:normal;color:var(--navy)}
  .heart{position:absolute;color:var(--yellow)}

  .feat{position:absolute;text-align:center;font-weight:500;color:var(--ink);line-height:1.1}
  .feat .ico{display:block;margin:0 auto .2em}
  .feat span{display:block}
  .c-violet{color:var(--violet)}
  .c-blue{color:var(--blue)}
  .c-yellow{color:#e3ad00}
  .c-red{color:var(--red)}
  .ico-navy{color:var(--navy)}
  .ico-yellow{color:#e9b400}
  .ico-red{color:var(--red)}
  .divider{position:absolute;border-left:1.5px dashed #b9b2d9}

  .badge{position:absolute;width:1em;height:1em;border-radius:50%;background:var(--violet);border:.035em solid var(--white);box-shadow:0 0 0 .012em var(--violet);color:var(--white);display:flex;flex-direction:column;align-items:center;justify-content:center;text-align:center}
  .badge .b-heart{width:.09em;height:.09em;color:var(--yellow);margin-bottom:.02em}
  .badge .b-tag{font-family:"Nunito",sans-serif;font-size:.068em;font-weight:600;line-height:1.25}
  .badge .b-script{font-family:"Kaushan Script",cursive;font-size:.13em;line-height:1.05;transform:rotate(-8deg);margin-top:.12em}
  .badge .b-script span{color:var(--yellow);display:block}

  .addr{position:absolute;color:var(--white);font-weight:500;line-height:1.25;display:flex;align-items:center;gap:.4em;letter-spacing:.01em}
  .addr svg{flex:none;width:1.4em;height:1.4em}
  .cta{position:absolute;background:var(--white);color:var(--navy);font-weight:600;display:flex;align-items:center;justify-content:center;gap:.45em;text-align:center;line-height:1.1;border-radius:999px}
  .cta .red{color:var(--red)}
  .cta svg{flex:none;width:1.4em;height:1.4em;color:var(--violet)}
  .cta.boxed{border-radius:4px;flex-direction:column;gap:.15em}
</style>
</head>
<body>
<div class="board">

<svg class="sprite" aria-hidden="true" focusable="false">
  <defs>
    <linearGradient id="photo-tone" x1="0" y1="0" x2="1" y2="1">
      <stop offset="0" stop-color="#e6e0dc"/>
      <stop offset=".35" stop-color="#e4bdc5"/>
      <stop offset=".65" stop-color="#cdab96"/>
      <stop offset="1" stop-color="#efe9e4"/>
    </linearGradient>
    <symbol id="i-people" viewBox="0 0 48 48"><g fill="none" stroke="currentColor" stroke-width="2.6" stroke-linecap="round" stroke-linejoin="round"><circle cx="18" cy="14" r="7"/><path d="M5 41c0-9 6-15 13-15s13 6 13 15z"/><circle cx="33" cy="20" r="5"/><path d="M31 41h12c0-7-4-11-10-11"/></g></symbol>
    <symbol id="i-cal" viewBox="0 0 48 48"><g fill="none" stroke="currentColor" stroke-width="2.6" stroke-linecap="round" stroke-linejoin="round"><rect x="5" y="9" width="38" height="33" rx="3"/><path d="M5 17h38M14 5v8M34 5v8"/><rect x="10" y="22" width="5" height="4"/><rect x="18" y="22" width="5" height="4"/><rect x="26" y="22" width="5" height="4"/><rect x="34" y="22" width="4" height="4"/><rect x="10" y="31" width="5" height="4"/><rect x="18" y="31" width="5" height="4"/><rect x="26" y="31" width="5" height="4"/><rect x="34" y="31" width="4" height="4"/></g></symbol>
    <symbol id="i-child" viewBox="0 0 48 48"><g fill="none" stroke="currentColor" stroke-width="2.6" stroke-linecap="round" stroke-linejoin="round"><circle cx="22" cy="15" r="8"/><path d="M8 43c0-9 6-15 14-15s14 6 14 15"/><path d="M33 36l3 3 7-8"/></g></symbol>
    <symbol id="i-doc" viewBox="0 0 48 48"><g fill="none" stroke="currentColor" stroke-width="2.6" stroke-linecap="round" stroke-linejoin="round"><circle cx="22" cy="12" r="7"/><path d="M6 44c0-10 7-16 16-16s16 6 16 16"/><path d="M17 28l5 9 5-9"/><path d="M36 31h7v5c0 4-3.5 6-3.5 6S36 40 36 36z"/></g></symbol>
    <symbol id="i-heart" viewBox="0 0 48 48"><g fill="none" stroke="currentColor" stroke-width="2.6" stroke-linecap="round" stroke-linejoin="round"><path d="M24 42C10 32 5 25 5 17a9.5 9.5 0 0 1 19-3 9.5 9.5 0 0 1 19 3c0 8-5 15-19 25z"/><path d="M24 31c-6-4-8-7-8-10a4 4 0 0 1 8-1 4 4 0 0 1 8 1c0 3-2 6-8 10z"/></g></symbol>
    <symbol id="i-pin" viewBox="0 0 48 48"><g fill="none" stroke="currentColor" stroke-width="3" stroke-linecap="round" stroke-linejoin="round"><path d="M24 44s13-14 13-25a13 13 0 0 0-26 0c0 11 13 25 13 25z"/><circle cx="24" cy="19" r="5"/></g></symbol>
    <symbol id="i-heart-fill" viewBox="0 0 48 48"><path fill="currentColor" d="M24 42C10 32 5 25 5 17a9.5 9.5 0 0 1 19-3 9.5 9.5 0 0 1 19 3c0 8-5 15-19 25z"/></symbol>
  </defs>
</svg>

<!-- ===== 160 x 160 ===== -->
<div class="ad ad-160" style="left:50px;top:49px;width:160px;height:160px">
  <svg class="layer" width="160" height="160" role="img" aria-label="Photo of a pediatrician examining a toddler with mother and sister"><path fill="url(#photo-tone)" d="M92 0C85 25 88 50 100 68L160 68L160 0Z"/></svg>
  <svg class="layer" width="160" height="160" aria-hidden="true"><path fill="none" stroke="var(--violet)" stroke-width="3" d="M92 0C85 25 88 50 100 68"/><path fill="var(--violet)" d="M0 126C50 122 110 128 160 118L160 160L0 160Z"/></svg>
  <div class="brand-mark" style="left:4px;top:5px;width:13px;height:13px"></div>
  <div class="brand-name" style="left:20px;top:3px;font-size:8.5px">Larkmont<br>Pediatrics</div>
  <div class="h-sher" style="left:2px;top:28px;font-size:9px">SHERWOOD'S</div>
  <div class="h-first" style="left:2px;top:38px;font-size:13.5px">FIRST &amp; <span class="red">ONLY</span></div>
  <div class="h-ded" style="left:2px;top:55px;font-size:4.6px">DEDICATED PEDIATRIC CLINIC</div>
  <div class="pin-ring" style="left:2px;top:71px;width:15px;height:15px;border-width:1px"><svg><use href="#i-pin"/></svg></div>
  <div class="open-band" style="left:14px;top:73px;width:126px;height:12px;font-size:6.5px"><b>NOW OPEN</b> IN SHERWOOD!</div>
  <div class="feat" style="left:0;top:91px;width:32px;font-size:3.8px"><svg class="ico ico-navy" width="13" height="13"><use href="#i-people"/></svg><span>ACCEPTING</span><span class="c-violet">NEW PATIENTS</span></div>
  <div class="feat" style="left:32px;top:91px;width:32px;font-size:3.8px"><svg class="ico ico-navy" width="13" height="13"><use href="#i-cal"/></svg><span>SAME-DAY</span><span class="c-blue">SICK VISITS</span></div>
  <div class="feat" style="left:64px;top:91px;width:32px;font-size:3.8px"><svg class="ico ico-yellow" width="13" height="13"><use href="#i-child"/></svg><span>WELL-CHILD</span><span class="c-yellow">CHECKUPS</span></div>
  <div class="feat" style="left:96px;top:91px;width:32px;font-size:3.8px"><svg class="ico ico-navy" width="13" height="13"><use href="#i-doc"/></svg><span>EXPERIENCED</span><span class="c-violet">EXPERTS</span></div>
  <div class="feat" style="left:128px;top:91px;width:32px;font-size:3.8px"><svg class="ico ico-red" width="13" height="13"><use href="#i-heart"/></svg><span>BEHAVIORAL</span><span class="c-red">HEALTH</span></div>
  <div class="addr" style="left:4px;top:133px;width:104px;font-size:4.4px"><svg><use href="#i-pin"/></svg>18250 SW ALDER CREST PKWY STE B-210, SHERWOOD, OR 97140, UNITED STATES</div>
  <div class="cta boxed" style="left:111px;top:129px;width:46px;height:27px;font-size:5px">SCHEDULE <span>YOUR <span class="red">FIRST</span></span><span><span class="red">VISIT</span> TODAY!</span></div>
</div>
<div class="size-label" style="left:21px;top:115px">160X160</div>

<!-- ===== 180 x 180 ===== -->
<div class="ad ad-180" style="left:50px;top:138px;width:180px;height:180px">
  <svg class="layer" width="180" height="180" role="img" aria-label="Photo of a pediatrician examining a toddler with mother and sister"><path fill="url(#photo-tone)" d="M102 0C94 30 96 62 108 92L180 92L180 0Z"/></svg>
  <svg class="layer" width="180" height="180" aria-hidden="true"><path fill="none" stroke="var(--violet)" stroke-width="3" d="M102 0C94 30 96 62 108 92"/><path fill="var(--violet)" d="M0 146C60 140 120 148 180 138L180 180L0 180Z"/></svg>
  <div class="brand-mark" style="left:4px;top:5px;width:15px;height:15px"></div>
  <div class="brand-name" style="left:23px;top:3px;font-size:9.5px">Larkmont<br>Pediatrics</div>
  <div class="h-sher" style="left:2px;top:32px;font-size:10px">SHERWOOD'S</div>
  <div class="h-first" style="left:2px;top:43px;font-size:14.5px">FIRST &amp; <span class="red">ONLY</span></div>
  <div class="h-ded" style="left:2px;top:62px;font-size:5.6px;white-space:normal;width:90px">DEDICATED PEDIATRIC CLINIC</div>
  <div class="pin-ring" style="left:2px;top:86px;width:17px;height:17px;border-width:1px"><svg><use href="#i-pin"/></svg></div>
  <div class="open-band" style="left:16px;top:88px;width:160px;height:13px;font-size:7px"><b>NOW OPEN</b> IN SHERWOOD!</div>
  <div class="feat" style="left:0;top:107px;width:36px;font-size:4.3px"><svg class="ico ico-navy" width="15" height="15"><use href="#i-people"/></svg><span>ACCEPTING</span><span class="c-violet">NEW PATIENTS</span></div>
  <div class="feat" style="left:36px;top:107px;width:36px;font-size:4.3px"><svg class="ico ico-navy" width="15" height="15"><use href="#i-cal"/></svg><span>SAME-DAY</span><span class="c-blue">SICK VISITS</span></div>
  <div class="feat" style="left:72px;top:107px;width:36px;font-size:4.3px"><svg class="ico ico-yellow" width="15" height="15"><use href="#i-child"/></svg><span>WELL-CHILD</span><span class="c-yellow">CHECKUPS</span></div>
  <div class="feat" style="left:108px;top:107px;width:36px;font-size:4.3px"><svg class="ico ico-navy" width="15" height="15"><use href="#i-doc"/></svg><span>EXPERIENCED</span><span class="c-violet">EXPERTS</span></div>
  <div class="feat" style="left:144px;top:107px;width:36px;font-size:4.3px"><svg class="ico ico-red" width="15" height="15"><use href="#i-heart"/></svg><span>BEHAVIORAL</span><span class="c-red">HEALTH</span></div>
  <div class="addr" style="left:4px;top:154px;width:118px;font-size:4.8px"><svg><use href="#i-pin"/></svg>18250 SW ALDER CREST PKWY STE B-210, SHERWOOD, OR 97140, UNITED STATES</div>
  <div class="cta boxed" style="left:127px;top:149px;width:49px;height:28px;font-size:5.3px">SCHEDULE <span>YOUR <span class="red">FIRST</span></span><span><span class="red">VISIT</span> TODAY!</span></div>
</div>
<div class="size-label" style="left:25px;top:211px">180X180</div>

<!-- ===== 300 x 250 ===== -->
<div class="ad ad-300" style="left:50px;top:234px;width:300px;height:250px">
  <svg class="layer" width="300" height="250" role="img" aria-label="Photo of a pediatrician examining a toddler with mother and sister"><path fill="url(#photo-tone)" d="M156 0C146 40 148 90 172 118L300 118L300 0Z"/></svg>
  <svg class="layer" width="300" height="250" aria-hidden="true"><path fill="none" stroke="var(--violet)" stroke-width="4" d="M156 0C146 40 148 90 172 118"/><path fill="var(--violet)" d="M0 222C90 216 200 222 300 208L300 250L0 250Z"/></svg>
  <div class="brand-mark" style="left:8px;top:13px;width:24px;height:24px"></div>
  <div class="brand-name" style="left:38px;top:10px;font-size:15px">Larkmont<br>Pediatrics</div>
  <div class="h-sher" style="left:6px;top:53px;font-size:16px">SHERWOOD'S</div>
  <div class="h-first" style="left:6px;top:72px;font-size:24px">FIRST &amp; <span class="red">ONLY</span></div>
  <div class="h-ded" style="left:6px;top:103px;font-size:8.3px">DEDICATED PEDIATRIC CLINIC</div>
  <div class="pin-ring" style="left:4px;top:119px;width:26px;height:26px;border-width:1.5px"><svg><use href="#i-pin"/></svg></div>
  <div class="open-band" style="left:24px;top:123px;width:206px;height:19px;font-size:11px"><b>NOW OPEN</b> IN SHERWOOD!</div>
  <svg class="heart" style="left:30px;top:149px;width:9px;height:9px"><use href="#i-heart-fill"/></svg>
  <div class="care" style="left:42px;top:149px;font-size:7.8px">Compassionate care for <em>newborns, children &amp; teens.</em></div>
  <div class="feat" style="left:1px;top:164px;width:66px;font-size:6.2px"><svg class="ico ico-navy" width="24" height="24"><use href="#i-people"/></svg><span>ACCEPTING</span><span class="c-violet">NEW PATIENTS</span></div>
  <div class="divider" style="left:68px;top:168px;height:44px"></div>
  <div class="feat" style="left:70px;top:164px;width:66px;font-size:6.2px"><svg class="ico ico-navy" width="24" height="24"><use href="#i-doc"/></svg><span>EXPERIENCED</span><span class="c-violet">PEDIATRIC EXPERTS</span></div>
  <div class="divider" style="left:138px;top:168px;height:44px"></div>
  <div class="feat" style="left:140px;top:164px;width:66px;font-size:6.2px"><svg class="ico ico-yellow" width="24" height="24"><use href="#i-child"/></svg><span>WELL-CHILD</span><span class="c-yellow">CHECKUPS</span></div>
  <div class="divider" style="left:208px;top:168px;height:44px"></div>
  <div class="feat" style="left:211px;top:164px;width:66px;font-size:6.2px"><svg class="ico ico-red" width="24" height="24"><use href="#i-heart"/></svg><span>BEHAVIORAL</span><span class="c-red">HEALTH</span></div>
  <div class="badge" style="left:250px;top:86px;font-size:48px"><svg class="b-heart"><use href="#i-heart-fill"/></svg><div class="b-tag">Healthy Kids.<br>Happier Futures.</div><div class="b-script">Right Here in<span>Sherwood!</span></div></div>
  <div class="addr" style="left:6px;top:230px;width:165px;font-size:5.8px"><svg><use href="#i-pin"/></svg>18250 SW ALDER CREST PKWY STE B-210, SHERWOOD, OR 97140, UNITED STATES</div>
  <div class="cta" style="left:176px;top:226px;width:120px;height:20px;font-size:6.6px;border-radius:4px"><svg><use href="#i-cal"/></svg><span>SCHEDULE YOUR <span class="red">FIRST</span><br><span class="red">VISIT</span> TODAY!</span></div>
</div>
<div class="size-label" style="left:48px;top:336px">300X250</div>

<!-- ===== 336 x 280 ===== -->
<div class="ad ad-336" style="left:50px;top:359px;width:336px;height:280px">
  <svg class="layer" width="336" height="280" role="img" aria-label="Photo of a pediatrician examining a toddler with mother and sister"><path fill="url(#photo-tone)" d="M172 0C160 45 162 100 188 133L336 133L336 0Z"/></svg>
  <svg class="layer" width="336" height="280" aria-hidden="true"><path fill="none" stroke="var(--violet)" stroke-width="4" d="M172 0C160 45 162 100 188 133"/><path fill="var(--violet)" d="M0 250C100 244 220 250 336 236L336 280L0 280Z"/></svg>
  <div class="brand-mark" style="left:8px;top:15px;width:28px;height:28px"></div>
  <div class="brand-name" style="left:43px;top:12px;font-size:17px">Larkmont<br>Pediatrics</div>
  <div class="h-sher" style="left:6px;top:64px;font-size:18px">SHERWOOD'S</div>
  <div class="h-first" style="left:6px;top:86px;font-size:27px">FIRST &amp; <span class="red">ONLY</span></div>
  <div class="h-ded" style="left:6px;top:119px;font-size:9.2px">DEDICATED PEDIATRIC CLINIC</div>
  <div class="pin-ring" style="left:4px;top:134px;width:29px;height:29px;border-width:1.5px"><svg><use href="#i-pin"/></svg></div>
  <div class="open-band" style="left:26px;top:138px;width:234px;height:22px;font-size:13px"><b>NOW OPEN</b> IN SHERWOOD!</div>
  <svg class="heart" style="left:32px;top:166px;width:10px;height:10px"><use href="#i-heart-fill"/></svg>
  <div class="care" style="left:45px;top:166px;font-size:8.8px">Compassionate care for <em>newborns, children &amp; teens.</em></div>
  <div class="feat" style="left:0;top:182px;width:74px;font-size:6.8px"><svg class="ico ico-navy" width="27" height="27"><use href="#i-people"/></svg><span>ACCEPTING</span><span class="c-violet">NEW PATIENTS</span></div>
  <div class="divider" style="left:79px;top:186px;height:50px"></div>
  <div class="feat" style="left:85px;top:182px;width:80px;font-size:6.8px"><svg class="ico ico-navy" width="27" height="27"><use href="#i-doc"/></svg><span>EXPERIENCED</span><span class="c-violet">PEDIATRIC EXPERTS</span></div>
  <div class="divider" style="left:170px;top:186px;height:50px"></div>
  <div class="feat" style="left:177px;top:182px;width:74px;font-size:6.8px"><svg class="ico ico-yellow" width="27" height="27"><use href="#i-child"/></svg><span>WELL-CHILD</span><span class="c-yellow">CHECKUPS</span></div>
  <div class="divider" style="left:253px;top:186px;height:50px"></div>
  <div class="feat" style="left:256px;top:182px;width:66px;font-size:6.8px"><svg class="ico ico-red" width="27" height="27"><use href="#i-heart"/></svg><span>BEHAVIORAL</span><span class="c-red">HEALTH</span></div>
  <div class="badge" style="left:270px;top:101px;font-size:60px"><svg class="b-heart"><use href="#i-heart-fill"/></svg><div class="b-tag">Healthy Kids.<br>Happier Futures.</div><div class="b-script">Right Here in<span>Sherwood!</span></div></div>
  <div class="addr" style="left:6px;top:257px;width:185px;font-size:6.4px"><svg><use href="#i-pin"/></svg>18250 SW ALDER CREST PKWY STE B-210, SHERWOOD, OR 97140, UNITED STATES</div>
  <div class="cta" style="left:194px;top:252px;width:138px;height:23px;font-size:7.6px;border-radius:4px"><svg><use href="#i-cal"/></svg><span>SCHEDULE YOUR<br><span class="red">FIRST VISIT</span> TODAY!</span></div>
</div>
<div class="size-label" style="left:55px;top:477px">336X280</div>

<!-- ===== 728 x 90 ===== -->
<div class="ad ad-728" style="left:222px;top:48px;width:728px;height:90px">
  <svg class="layer" width="728" height="90" role="img" aria-label="Photo of a pediatrician examining a toddler with mother and sister"><path fill="url(#photo-tone)" d="M578 0C566 30 566 60 578 90L728 90L728 0Z"/></svg>
  <svg class="layer" width="728" height="90" aria-hidden="true"><path fill="none" stroke="var(--violet)" stroke-width="5" d="M578 0C566 30 566 60 578 90"/><path fill="var(--violet)" d="M335 90L346 64C420 60 500 58 568 38L578 90Z"/></svg>
  <div class="brand-mark" style="left:28px;top:7px;width:22px;height:22px"></div>
  <div class="brand-name" style="left:56px;top:5px;font-size:13px">Larkmont<br>Pediatrics</div>
  <div class="h-sher center" style="left:10px;top:39px;width:160px;font-size:11px">SHERWOOD'S</div>
  <div class="h-first center" style="left:10px;top:51px;width:160px;font-size:22px">FIRST &amp; <span class="red">ONLY</span></div>
  <div class="h-ded center" style="left:10px;top:75px;width:160px;font-size:7px">DEDICATED PEDIATRIC CLINIC</div>
  <div class="feat" style="left:167px;top:6px;width:58px;font-size:6px"><svg class="ico ico-navy" width="22" height="22"><use href="#i-people"/></svg><span>ACCEPTING</span><span class="c-violet">NEW PATIENTS</span></div>
  <div class="feat" style="left:227px;top:6px;width:58px;font-size:6px"><svg class="ico ico-navy" width="22" height="22"><use href="#i-cal"/></svg><span>SAME-DAY</span><span class="c-blue">SICK VISITS</span></div>
  <div class="feat" style="left:287px;top:6px;width:58px;font-size:6px"><svg class="ico ico-yellow" width="22" height="22"><use href="#i-child"/></svg><span>WELL-CHILD</span><span class="c-yellow">CHECKUPS</span></div>
  <div class="feat" style="left:347px;top:6px;width:76px;font-size:6px"><svg class="ico ico-navy" width="22" height="22"><use href="#i-doc"/></svg><span>EXPERIENCED</span><span class="c-violet">PEDIATRIC EXPERTS</span></div>
  <div class="feat" style="left:428px;top:6px;width:58px;font-size:6px"><svg class="ico ico-red" width="22" height="22"><use href="#i-heart"/></svg><span>BEHAVIORAL</span><span class="c-red">HEALTH</span></div>
  <div class="pin-ring" style="left:172px;top:56px;width:17px;height:17px;border-width:1px"><svg><use href="#i-pin"/></svg></div>
  <div class="open-band" style="left:186px;top:59px;width:141px;height:12px;font-size:7.5px"><b>NOW OPEN</b> IN SHERWOOD!</div>
  <div class="care center" style="left:172px;top:74px;width:160px;font-size:6.2px">Compassionate care for <em>newborns,<br>children &amp; teens.</em></div>
  <div class="addr" style="left:362px;top:66px;width:126px;font-size:5.4px"><svg><use href="#i-pin"/></svg>18250 SW ALDER CREST PKWY STE B-210, SHERWOOD, OR 97140, UNITED STATES</div>
  <div class="cta boxed" style="left:494px;top:56px;width:68px;height:30px;font-size:6px"><svg style="width:9px;height:9px"><use href="#i-cal"/></svg><span>SCHEDULE YOUR</span><span><span class="red">FIRST VISIT</span> TODAY!</span></div>
  <div class="badge" style="left:549px;top:-5px;font-size:44px"><svg class="b-heart"><use href="#i-heart-fill"/></svg><div class="b-tag">Healthy Kids.<br>Happier Futures.</div><div class="b-script">Right Here in<span>Sherwood!</span></div></div>
</div>
<div class="size-label" style="left:303px;top:88px">728X90</div>

<!-- ===== 920 x 250 ===== -->
<div class="ad ad-920" style="left:222px;top:105px;width:920px;height:250px">
  <svg class="layer" width="920" height="250" role="img" aria-label="Photo of a pediatrician examining a toddler with mother and sister"><path fill="url(#photo-tone)" d="M575 0C548 55 545 125 585 172C620 208 670 214 730 210L920 198L920 0Z"/></svg>
  <svg class="layer" width="920" height="250" aria-hidden="true"><path fill="none" stroke="var(--violet)" stroke-width="10" d="M575 0C548 55 545 125 585 172C620 208 670 214 730 210"/><path fill="var(--violet-soft)" opacity=".55" d="M0 202C250 192 500 186 700 192C800 194 880 178 920 160L920 250L0 250Z"/><path fill="var(--violet)" d="M0 210C250 202 500 198 700 203C800 205 880 190 920 176L920 250L0 250Z"/></svg>
  <div class="brand-mark" style="left:64px;top:12px;width:44px;height:44px"></div>
  <div class="brand-name" style="left:117px;top:9px;font-size:24px">Larkmont<br>Pediatrics</div>
  <div class="h-sher center" style="left:0;top:73px;width:330px;font-size:22px">SHERWOOD'S</div>
  <div class="h-first center" style="left:0;top:98px;width:330px;font-size:41px">FIRST &amp; <span class="red">ONLY</span></div>
  <div class="h-ded center" style="left:0;top:140px;width:330px;font-size:15px">DEDICATED PEDIATRIC CLINIC</div>
  <svg class="heart" style="left:60px;top:170px;width:12px;height:12px"><use href="#i-heart-fill"/></svg>
  <div class="care center" style="left:65px;top:170px;width:230px;font-size:11.5px">Compassionate care for <em>newborns,<br>children &amp; teens.</em></div>
  <div class="feat" style="left:311px;top:20px;width:80px;font-size:9px"><svg class="ico ico-navy" width="32" height="32"><use href="#i-people"/></svg><span>ACCEPTING</span><span class="c-violet">NEW PATIENTS</span></div>
  <div class="divider" style="left:392px;top:24px;height:46px"></div>
  <div class="feat" style="left:392px;top:20px;width:80px;font-size:9px"><svg class="ico ico-navy" width="32" height="32"><use href="#i-cal"/></svg><span>SAME-DAY</span><span class="c-blue">SICK VISITS</span></div>
  <div class="divider" style="left:472px;top:24px;height:46px"></div>
  <div class="feat" style="left:466px;top:20px;width:80px;font-size:9px"><svg class="ico ico-yellow" width="32" height="32"><use href="#i-child"/></svg><span>WELL-CHILD</span><span class="c-yellow">CHECKUPS</span></div>
  <div class="feat" style="left:335px;top:90px;width:100px;font-size:9px"><svg class="ico ico-navy" width="32" height="32"><use href="#i-doc"/></svg><span>EXPERIENCED</span><span class="c-violet">PEDIATRIC EXPERTS</span></div>
  <div class="divider" style="left:436px;top:94px;height:46px"></div>
  <div class="feat" style="left:435px;top:90px;width:80px;font-size:9px"><svg class="ico ico-red" width="32" height="32"><use href="#i-heart"/></svg><span>BEHAVIORAL</span><span class="c-red">HEALTH</span></div>
  <div class="pin-ring" style="left:298px;top:160px;width:34px;height:34px;border-width:1.5px"><svg><use href="#i-pin"/></svg></div>
  <div class="open-band" style="left:326px;top:165px;width:232px;height:24px;font-size:14px"><b>NOW OPEN</b> IN SHERWOOD!</div>
  <div class="badge" style="left:824px;top:-3px;font-size:88px"><svg class="b-heart"><use href="#i-heart-fill"/></svg><div class="b-tag">Healthy Kids.<br>Happier Futures.</div><div class="b-script">Right Here in<span>Sherwood!</span></div></div>
  <div class="addr" style="left:26px;top:220px;font-size:10px;white-space:nowrap"><svg><use href="#i-pin"/></svg>18250 SW ALDER CREST PKWY STE B-210, SHERWOOD, OR 97140, UNITED STATES</div>
  <div class="cta" style="left:648px;top:212px;width:248px;height:24px;font-size:10.5px"><svg><use href="#i-cal"/></svg><span>SCHEDULE YOUR <span class="red">FIRST VISIT</span> TODAY!</span></div>
</div>
<div class="size-label" style="left:341px;top:208px">900X250</div>

<!-- ===== 1200 x 627 ===== -->
<div class="ad ad-1200" style="left:222px;top:225px;width:1200px;height:627px">
  <svg class="layer" width="1200" height="627" role="img" aria-label="Photo of a smiling pediatrician with stethoscope examining a toddler on his mother's lap, with an older sister holding a plush toy"><path fill="url(#photo-tone)" d="M560 0C495 170 490 340 600 420C680 480 720 520 860 525L1200 490L1200 0Z"/></svg>
  <svg class="layer" width="1200" height="627" aria-hidden="true">
    <path fill="none" stroke="var(--violet)" stroke-width="20" d="M560 0C495 170 490 340 600 420C680 480 720 520 860 525"/>
    <path fill="var(--violet-soft)" opacity=".55" d="M0 540C300 520 500 505 700 518C900 532 1050 480 1200 420L1200 627L0 627Z"/>
    <path fill="var(--violet)" d="M0 560C200 545 420 522 620 535C820 548 1000 500 1200 445L1200 627L0 627Z"/>
  </svg>
  <div class="brand-mark" style="left:72px;top:34px;width:96px;height:96px"></div>
  <div class="brand-name" style="left:190px;top:30px;font-size:52px">Larkmont<br>Pediatrics</div>
  <div class="h-sher center" style="left:0;top:150px;width:530px;font-size:46px">SHERWOOD'S</div>
  <div class="h-first center" style="left:0;top:203px;width:530px;font-size:70px">FIRST &amp; <span class="red">ONLY</span></div>
  <div class="h-ded center" style="left:0;top:280px;width:530px;font-size:27px">DEDICATED PEDIATRIC CLINIC</div>
  <div class="pin-ring" style="left:26px;top:314px;width:54px;height:54px;border-width:2.5px"><svg><use href="#i-pin"/></svg></div>
  <div class="open-band" style="left:72px;top:322px;width:426px;height:38px;font-size:27px"><b>NOW OPEN</b> IN SHERWOOD!</div>
  <svg class="heart" style="left:38px;top:376px;width:24px;height:24px"><use href="#i-heart-fill"/></svg>
  <div class="care center" style="left:40px;top:374px;width:470px;font-size:23px">Compassionate care for <em>newborns,<br>children &amp; teens.</em></div>
  <div class="feat" style="left:10px;top:442px;width:122px;font-size:13.5px"><svg class="ico ico-navy" width="52" height="52"><use href="#i-people"/></svg><span>ACCEPTING</span><span class="c-violet">NEW PATIENTS</span></div>
  <div class="divider" style="left:131px;top:450px;height:78px"></div>
  <div class="feat" style="left:130px;top:442px;width:118px;font-size:13.5px"><svg class="ico ico-navy" width="52" height="52"><use href="#i-cal"/></svg><span>SAME-DAY</span><span class="c-blue">SICK VISITS</span></div>
  <div class="divider" style="left:252px;top:450px;height:78px"></div>
  <div class="feat" style="left:256px;top:442px;width:118px;font-size:13.5px"><svg class="ico ico-yellow" width="52" height="52"><use href="#i-child"/></svg><span>WELL-CHILD</span><span class="c-yellow">CHECKUPS</span></div>
  <div class="divider" style="left:381px;top:450px;height:78px"></div>
  <div class="feat" style="left:381px;top:442px;width:144px;font-size:13.5px"><svg class="ico ico-navy" width="52" height="52"><use href="#i-doc"/></svg><span>EXPERIENCED</span><span class="c-violet">PEDIATRIC EXPERTS</span></div>
  <div class="divider" style="left:525px;top:450px;height:78px"></div>
  <div class="feat" style="left:533px;top:442px;width:120px;font-size:13.5px"><svg class="ico ico-red" width="52" height="52"><use href="#i-heart"/></svg><span>BEHAVIORAL</span><span class="c-red">HEALTH</span></div>
  <div class="badge" style="left:1017px;top:7px;font-size:172px"><svg class="b-heart"><use href="#i-heart-fill"/></svg><div class="b-tag">Healthy Kids.<br>Happier Futures.</div><div class="b-script">Right Here in<span>Sherwood!</span></div></div>
  <div class="addr" style="left:24px;top:588px;font-size:13.5px;white-space:nowrap"><svg><use href="#i-pin"/></svg>18250 SW ALDER CREST PKWY STE B-210, SHERWOOD, OR 97140, UNITED STATES</div>
  <div class="cta" style="left:737px;top:566px;width:431px;height:42px;font-size:19px"><svg><use href="#i-cal"/></svg><span>SCHEDULE YOUR <span class="red">FIRST VISIT</span> TODAY!</span></div>
</div>
<div class="size-label big" style="left:335px;top:496px">1200X627</div>

<!-- ===== 1080 x 1080 ===== -->
<div class="ad ad-1080" style="left:730px;top:48px;width:1080px;height:1080px">
  <svg class="layer" width="1080" height="1080" role="img" aria-label="Photo of a smiling pediatrician with stethoscope examining a toddler on his mother's lap"><path fill="url(#photo-tone)" d="M600 0C520 240 450 480 470 690C490 870 600 940 760 940L1080 900L1080 0Z"/></svg>
  <svg class="layer" width="1080" height="1080" aria-hidden="true">
    <path fill="none" stroke="var(--violet)" stroke-width="24" d="M600 0C520 240 450 480 470 690C490 870 600 940 760 940"/>
    <path fill="var(--violet-soft)" opacity=".55" d="M0 965C250 930 560 980 820 955C950 942 1030 900 1080 860L1080 1080L0 1080Z"/>
    <path fill="var(--violet)" d="M0 985C250 952 560 1000 820 975C950 962 1030 922 1080 882L1080 1080L0 1080Z"/>
  </svg>
  <div class="brand-mark" style="left:42px;top:40px;width:110px;height:110px"></div>
  <div class="brand-name" style="left:178px;top:32px;font-size:60px">Larkmont<br>Pediatrics</div>
  <div class="h-sher center" style="left:0;top:162px;width:560px;font-size:52px">SHERWOOD'S</div>
  <div class="h-first center" style="left:0;top:212px;width:560px;font-size:78px">FIRST &amp; <span class="red">ONLY</span></div>
  <div class="h-ded center" style="left:0;top:294px;width:560px;font-size:32px">DEDICATED PEDIATRIC CLINIC</div>
  <div class="pin-ring" style="left:199px;top:340px;width:86px;height:86px;border-width:3px"><svg><use href="#i-pin"/></svg></div>
  <div class="open-box" style="left:42px;top:414px;width:400px;height:171px;font-size:58px"><div><b>NOW OPEN</b> IN</div><div>SHERWOOD!</div></div>
  <svg class="heart" style="left:42px;top:612px;width:44px;height:44px"><use href="#i-heart-fill"/></svg>
  <div class="care center" style="left:86px;top:604px;width:380px;font-size:30px">Compassionate care for<br><em>newborns, children &amp;<br>teens.</em></div>
  <div class="feat" style="left:12px;top:718px;width:150px;font-size:17px"><svg class="ico ico-navy" width="62" height="62"><use href="#i-people"/></svg><span>ACCEPTING</span><span class="c-violet">NEW PATIENTS</span></div>
  <div class="divider" style="left:167px;top:722px;height:90px"></div>
  <div class="feat" style="left:166px;top:718px;width:150px;font-size:17px"><svg class="ico ico-navy" width="62" height="62"><use href="#i-cal"/></svg><span>SAME-DAY</span><span class="c-blue">SICK VISITS</span></div>
  <div class="divider" style="left:315px;top:722px;height:90px"></div>
  <div class="feat" style="left:315px;top:718px;width:150px;font-size:17px"><svg class="ico ico-yellow" width="62" height="62"><use href="#i-child"/></svg><span>WELL-CHILD</span><span class="c-yellow">CHECKUPS</span></div>
  <div class="feat" style="left:78px;top:850px;width:170px;font-size:17px"><svg class="ico ico-navy" width="62" height="62"><use href="#i-doc"/></svg><span>EXPERIENCED</span><span class="c-violet">PEDIATRIC EXPERTS</span></div>
  <div class="divider" style="left:262px;top:854px;height:90px"></div>
  <div class="feat" style="left:258px;top:850px;width:150px;font-size:17px"><svg class="ico ico-red" width="62" height="62"><use href="#i-heart"/></svg><span>BEHAVIORAL</span><span class="c-red">HEALTH</span></div>
  <div class="badge" style="left:521px;top:722px;font-size:186px"><svg class="b-heart"><use href="#i-heart-fill"/></svg><div class="b-tag">Healthy Kids.<br>Happier Futures.</div><div class="b-script">Right Here in<span>Sherwood!</span></div></div>
  <svg class="abs" style="left:160px;top:1006px;width:26px;height:26px;color:var(--white)" aria-hidden="true"><use href="#i-pin"/></svg>
  <div class="addr center" style="left:20px;top:1038px;width:340px;font-size:15px;display:block">18250 SW ALDER CREST PKWY STE B-210,<br>SHERWOOD, OR 97140, UNITED STATES</div>
  <div class="cta" style="left:587px;top:1013px;width:461px;height:50px;font-size:22px"><svg><use href="#i-cal"/></svg><span>SCHEDULE YOUR <span class="red">FIRST VISIT</span> TODAY!</span></div>
</div>
<div class="size-label big" style="left:820px;top:504px">1080X1080</div>

</div>
</body>
</html>
```